Business Card Design for Property Development Company Director

I am looking for a professional and unforgettable business card design for our Director of our Property Development Company.
Please see attached .pptx file to find out what information to include. You don't have to follow the exact format shown in the file - I am interested to see your creative flair using the information provided.

```html
<!DOCTYPE html>
<html lang="en">
<head>
<meta charset="utf-8">
<title>Kestrel Property Group – Business Card</title>
<link rel="stylesheet" href="https://fonts.googleapis.com/css2?family=Lato:wght@400;700&display=swap">
<style>
  :root {
    --canvas: #e9e6e1;
    --card-front: #ffffff;
    --card-back: #636363;
    --ink-grey: #5e5e5e;
    --brand-blue: #1f57a8;
    --white: #ffffff;
  }
  * { margin: 0; padding: 0; box-sizing: border-box; }
  html, body { width: 1200px; height: 848px; overflow: hidden; }
  body {
    background: var(--canvas);
    font-family: "Lato", sans-serif;
    position: relative;
  }
  .card {
    position: absolute;
    left: 251px;
    width: 674px;
    height: 378px;
    box-shadow: 0 4px 14px rgba(0,0,0,0.18);
  }
  .card--front { top: 28px; background: var(--card-front); color: var(--ink-grey); }
  .card--back { top: 442px; background: var(--card-back); color: var(--white); text-align: center; }

  .brand {
    position: absolute;
    display: flex;
    align-items: center;
    gap: 12px;
    font-weight: 700;
    letter-spacing: 0.5px;
    white-space: nowrap;
  }
  .brand__square { width: 34px; height: 34px; flex: none; }
  .card--front .brand { right: 38px; top: 72px; font-size: 26px; color: var(--brand-blue); }
  .card--front .brand__square { background: var(--brand-blue); }
  .card--back .brand {
    left: 50%; top: 196px; transform: translateX(-50%);
    font-size: 34px; color: var(--white);
  }
  .card--back .brand__square { width: 44px; height: 44px; background: var(--white); }

  .person { position: absolute; left: 37px; top: 159px; }
  .person__name { font-size: 21px; font-weight: 700; line-height: 1.2; }
  .person__name .surname { color: var(--brand-blue); }
  .person__role { font-size: 17px; line-height: 1.2; }

  .contact { position: absolute; left: 37px; top: 226px; list-style: none; }
  .contact li {
    display: flex; align-items: center; gap: 7px;
    font-size: 17px; line-height: 23px;
  }
  .contact svg { width: 13px; height: 13px; fill: var(--brand-blue); flex: none; }

  .licence { position: absolute; left: 36px; top: 323px; font-size: 17px; }

  .tagline {
    position: absolute; left: 0; right: 0; top: 74px;
    font-size: 23px; line-height: 28px;
  }
  .invite {
    position: absolute; left: 0; right: 0; top: 313px;
    font-size: 17px;
  }
</style>
</head>
<body>

<section class="card card--front" aria-label="Card front">
  <div class="brand"><span class="brand__square"></span><span>KESTREL PROPERTY GROUP</span></div>

  <div class="person">
    <p class="person__name">Daniel <span class="surname">Morrow</span></p>
    <p class="person__role">Director</p>
  </div>

  <ul class="contact">
    <li>
      <svg viewBox="0 0 24 24" aria-hidden="true"><path d="M6.6 10.8a15.1 15.1 0 0 0 6.6 6.6l2.2-2.2c.3-.3.7-.4 1-.2 1.1.4 2.3.6 3.6.6.6 0 1 .4 1 1V20c0 .6-.4 1-1 1A17 17 0 0 1 3 4c0-.6.4-1 1-1h3.5c.6 0 1 .4 1 1 0 1.3.2 2.5.6 3.6.1.3 0 .7-.2 1z"/></svg>
      <span>0400 123 456</span>
    </li>
    <li>
      <svg viewBox="0 0 24 24" aria-hidden="true"><path d="M2 5h20v14H2z" fill="none"/><path d="M2 5h20l-10 7z"/><path d="M2 7.5l10 7 10-7V19H2z"/></svg>
      <span>daniel@kestrelgroup.com.au</span>
    </li>
    <li>
      <svg viewBox="0 0 24 24" aria-hidden="true"><path d="M12 2a10 10 0 1 0 0 20 10 10 0 0 0 0-20zm6.9 6h-3a15.6 15.6 0 0 0-1.3-3.9A8 8 0 0 1 18.9 8zM12 4c.8 1.2 1.5 2.5 1.9 4h-3.8c.4-1.5 1.1-2.8 1.9-4zM4.3 14a8 8 0 0 1 0-4h3.4a16 16 0 0 0 0 4zm.8 2h3c.3 1.4.8 2.7 1.3 3.9A8 8 0 0 1 5.1 16zm3-8h-3a8 8 0 0 1 4.3-3.9C8.8 5.3 8.4 6.6 8.1 8zM12 20c-.8-1.2-1.5-2.5-1.9-4h3.8c-.4 1.5-1.1 2.8-1.9 4zm2.3-6H9.7a14.6 14.6 0 0 1 0-4h4.6a14.6 14.6 0 0 1 0 4zm.3 5.9c.6-1.2 1-2.5 1.3-3.9h3a8 8 0 0 1-4.3 3.9zm1.7-5.9a16 16 0 0 0 0-4h3.4a8 8 0 0 1 0 4z"/></svg>
      <span>www.kestrelgroup.com.au</span>
    </li>
  </ul>

  <p class="licence">Real Estate Lic: 4100235 &amp; 4100236</p>
</section>

<section class="card card--back" aria-label="Card back">
  <p class="tagline">Property Development<br>&amp; Site Acquisition Specialists</p>
  <div class="brand"><span class="brand__square"></span><span>KESTREL PROPERTY GROUP</span></div>
  <p class="invite">Ask me about our INVESTMENT &amp; PARTNERSHIP opportunities</p>
</section>

</body>
</html>
```